Flash Banners for CourseLantern.com

We are running a media campaign to drive traffic to CourseLantern.com. Course Lantern allows people that are interested in pursuing an advanced degree to find colleges and universities that offer their program and level of study.

We would like to have Flash Interactive banners created that grab people’s attention and have a high click-thru rate for our CPM Media Campaign.

BANNER MESSAGING/CLICKABLE ELEMENTS:
Headline: Earn Your Degree Online!

Clickable Elements with Rollover Animation and/or Icons:
GROUPING 1
Nursing
Business
Education
Legal
Design
And more
GROUPING 2
Associates
Bachelor’s
Master’s
Doctorate
(Each group should have some kind of visual separation, no need to label
Group1 or Group 2)

Call To Action: Find Schools

Logo: CourseLantern

Industry/Entity Type

Business

Requirements
Must have
• We would like animated flash banners in the following sizes:
300x250
728x90
160x600

The spec requirements are:
24 FPS (Frames per second)
30 seconds max animation, looping back to beginning
120K Max File Size
Final .swf file & Original .FLA file with layers

```html
<!DOCTYPE html>
<html lang="en">
<head>
<meta charset="utf-8">
<title>Course Lantern – Flash Animation Storyboard</title>
<link href="https://fonts.googleapis.com/css2?family=PT+Sans:wght@400;700&display=swap" rel="stylesheet">
<style>
  :root {
    --stage: #000000;
    --panel-light: #fbfbfb;
    --panel-mid: #e4e4e4;
    --bezel: #1a1a1a;
    --bezel-edge: #3a3a3a;
    --board-light: #4f7a5c;
    --board-dark: #2f5a3d;
    --chin-light: #f2f2f4;
    --chin-dark: #bfc0c4;
    --stand: #cfd0d4;
    --brand-ink: #1f4a66;
    --brand-accent: #e8621c;
    --cta-top: #f07a2a;
    --cta-bottom: #d4520f;
    --white: #ffffff;
    --cross: #c0281e;
    --leather: #2a2a2a;
    --book: #8fa6b3;
    --wood: #7a4322;
    --brush: #b5621f;
  }
  * { box-sizing: border-box; margin: 0; padding: 0; }
  html, body { width: 1200px; height: 900px; overflow: hidden; background: var(--stage); }
  body { position: relative; font-family: "PT Sans", "Helvetica Neue", Arial, sans-serif; }

  .board-title {
    position: absolute; top: 18px; left: 0; width: 1270px; text-align: center;
    color: var(--white); font-weight: 700; font-size: 19px; letter-spacing: 0.2px; word-spacing: 4px;
  }

  .banner {
    position: absolute; width: 300px; height: 250px; overflow: hidden;
    background: radial-gradient(ellipse at 50% 35%, var(--panel-light) 0%, var(--panel-mid) 100%);
  }

  .brand {
    position: absolute; top: 14px; left: 0; width: 100%;
    display: flex; justify-content: center; align-items: center; gap: 6px;
    font-size: 18px; font-weight: 700; color: var(--brand-ink); letter-spacing: -0.2px;
  }
  .brand-mark { width: 11px; height: 11px; background: var(--brand-accent); }

  .monitor {
    position: absolute; left: 8px; top: 40px; width: 284px; height: 170px;
    background: var(--bezel); border-radius: 8px 8px 0 0;
    box-shadow: inset 0 0 0 1px var(--bezel-edge);
  }
  .screen {
    position: absolute; left: 10px; top: 10px; width: 265px; height: 150px;
    background: radial-gradient(ellipse at 45% 40%, var(--board-light) 0%, var(--board-dark) 100%);
    display: flex; flex-direction: column; align-items: center; justify-content: center;
    color: var(--white); text-align: center; font-weight: 700;
    text-shadow: 0 2px 3px rgba(0,0,0,0.45);
  }
  .chin {
    position: absolute; left: 8px; top: 210px; width: 284px; height: 26px;
    background: linear-gradient(180deg, var(--chin-light), var(--chin-dark));
    border-radius: 0 0 6px 6px;
  }
  .stand {
    position: absolute; left: 119px; top: 236px; width: 62px; height: 14px;
    background: linear-gradient(180deg, #a9aaae, var(--stand));
  }

  .headline { font-size: 30px; line-height: 1.1; letter-spacing: -0.4px; }
  .topic { font-size: 37px; line-height: 1; letter-spacing: -0.4px; }
  .topic-icon { margin-bottom: 8px; }

  .icon-briefcase { width: 62px; height: 50px; border-radius: 6px; background: linear-gradient(180deg, #4a4a4a, var(--leather)); }
  .icon-book { width: 46px; height: 62px; border-radius: 3px; background: linear-gradient(90deg, #3a4a52 0 14%, var(--book) 14%); }
  .icon-gavel { width: 112px; height: 46px; border-radius: 4px; background: linear-gradient(90deg, #5e2e14, var(--wood)); }
  .icon-brush { width: 112px; height: 44px; border-radius: 22px; background: linear-gradient(90deg, #3a2516, var(--brush) 50%, #c9c9c9); }

  /* final frame */
  .banner--end .monitor { top: -10px; left: 10px; width: 282px; height: 155px; border-radius: 0; }
  .banner--end .screen { left: 9px; top: 10px; width: 265px; height: 136px; }
  .banner--end .chin { left: 10px; top: 145px; width: 282px; height: 27px; }
  .banner--end .stand {
    left: 105px; top: 172px; width: 92px; height: 33px; background: transparent;
  }
  .banner--end .headline { font-size: 34px; margin-top: -16px; }
  .banner--end .brand {
    top: auto; bottom: 8px; left: 12px; width: auto; justify-content: flex-start;
  }
  .cta {
    position: absolute; left: 174px; top: 212px; width: 115px; height: 31px;
    background: linear-gradient(180deg, var(--cta-top), var(--cta-bottom));
    color: var(--white); font-weight: 700; font-size: 16px;
    display: flex; align-items: center; justify-content: center; border-radius: 2px;
  }
</style>
</head>
<body>
  <h1 class="board-title">FLASH ANIMATION&nbsp; STORYBOARD</h1>

  <section class="banner" style="left:149px;top:62px">
    <div class="brand"><span>courselantern</span><span class="brand-mark"></span></div>
    <div class="monitor"><div class="screen"><p class="headline">Earn your<br>degree online!</p></div></div>
    <div class="chin"></div><div class="stand"></div>
  </section>

  <section class="banner" style="left:469px;top:62px">
    <div class="brand"><span>courselantern</span><span class="brand-mark"></span></div>
    <div class="monitor"><div class="screen">
      <svg class="topic-icon" width="50" height="50" viewBox="0 0 50 50" aria-hidden="true">
        <path d="M17 0h16v17h17v16H33v17H17V33H0V17h17z" fill="var(--cross)"/>
      </svg>
      <p class="topic">Nursing</p>
    </div></div>
    <div class="chin"></div><div class="stand"></div>
  </section>

  <section class="banner" style="left:789px;top:62px">
    <div class="brand"><span>courselantern</span><span class="brand-mark"></span></div>
    <div class="monitor"><div class="screen">
      <div class="topic-icon icon-briefcase" role="img" aria-label="Black leather briefcase"></div>
      <p class="topic">Business</p>
    </div></div>
    <div class="chin"></div><div class="stand"></div>
  </section>

  <section class="banner" style="left:149px;top:327px">
    <div class="brand"><span>courselantern</span><span class="brand-mark"></span></div>
    <div class="monitor"><div class="screen">
      <div class="topic-icon icon-book" role="img" aria-label="Closed hardcover book"></div>
      <p class="topic">Education</p>
    </div></div>
    <div class="chin"></div><div class="stand"></div>
  </section>

  <section class="banner" style="left:469px;top:327px">
    <div class="brand"><span>courselantern</span><span class="brand-mark"></span></div>
    <div class="monitor"><div class="screen">
      <div class="topic-icon icon-gavel" role="img" aria-label="Wooden judge's gavel"></div>
      <p class="topic">Legal</p>
    </div></div>
    <div class="chin"></div><div class="stand"></div>
  </section>

  <section class="banner" style="left:789px;top:327px">
    <div class="brand"><span>courselantern</span><span class="brand-mark"></span></div>
    <div class="monitor"><div class="screen">
      <div class="topic-icon icon-brush" role="img" aria-label="Artist's paintbrush"></div>
      <p class="topic">Design</p>
    </div></div>
    <div class="chin"></div><div class="stand"></div>
  </section>

  <section class="banner" style="left:149px;top:600px">
    <div class="brand"><span>courselantern</span><span class="brand-mark"></span></div>
    <div class="monitor"><div class="screen"><p class="topic">&amp; more</p></div></div>
    <div class="chin"></div><div class="stand"></div>
  </section>

  <section class="banner banner--end" style="left:458px;top:600px">
    <div class="monitor"><div class="screen"><p class="headline">earn your<br>degree online!</p></div></div>
    <div class="chin"></div>
    <svg class="stand" viewBox="0 0 92 33" aria-hidden="true">
      <path d="M24 0h44l6 24q18 4 18 9H0q0-5 18-9z" fill="var(--stand)"/>
    </svg>
    <div class="brand"><span>courselantern</span><span class="brand-mark"></span></div>
    <a class="cta">Find Schools</a>
  </section>
</body>
</html>
```